Restaurant Facility Equipment & Store Maintenance/

I need a flyer showing commercial/industrial kitchen equipment photos we work on Hot Equipment & Cold Equipment and offer many services. see attached highlights

```html
<!DOCTYPE html>
<html lang="en">
<head>
<meta charset="utf-8">
<title>Kitchen Equipment Services Flyer</title>
<link rel="stylesheet" href="https://fonts.googleapis.com/css2?family=Alfa+Slab+One&family=Poppins:wght@500;600;700&display=swap">
<style>
  :root {
    --slate: #44434f;
    --yellow: #ece51e;
    --white: #ffffff;
    --page: #ffffff;
  }
  * { margin: 0; padding: 0; box-sizing: border-box; }
  html, body { width: 1200px; height: 1200px; overflow: hidden; background: var(--page); }
  .flyer {
    position: absolute; left: 196px; top: 29px;
    width: 808px; height: 1142px;
    background: var(--slate);
    color: var(--white);
    font-family: "Poppins", sans-serif;
  }
  .headline-frame {
    position: absolute; left: 48px; top: 51px; width: 712px; height: 266px;
    border: 8px solid var(--yellow); border-radius: 42px;
  }
  .title-line {
    position: absolute; left: 0; width: 100%; text-align: center;
    font-family: "Alfa Slab One", serif; line-height: 1;
    text-shadow: 2px 3px 3px rgba(0,0,0,0.45);
  }
  .title-kicker { top: 86px; font-size: 30px; color: var(--white); }
  .title-main { top: 123px; font-size: 66px; color: var(--yellow); letter-spacing: -0.5px; }
  .title-sub { top: 189px; font-size: 48px; color: var(--yellow); }
  .tagline {
    position: absolute; left: 0; width: 100%; top: 264px; text-align: center;
    font-weight: 700; font-size: 19px; line-height: 24px;
  }
  .section-heading {
    position: absolute; left: 52px; top: 347px;
    font-weight: 700; font-size: 21px; line-height: 26px; color: var(--yellow);
  }
  .item {
    position: absolute; display: flex; align-items: center; gap: 11px;
  }
  .tick { width: 22px; height: 22px; flex: none; }
  .service-chip { font-weight: 600; font-size: 16px; line-height: 22px; text-transform: uppercase; }
  .feature { font-weight: 600; font-size: 14.6px; line-height: 17px; }
  .call-out {
    position: absolute; left: 420px; width: 360px; text-align: center;
    font-weight: 700; font-size: 17px; line-height: 22px;
  }
  .call-out--accent { color: var(--yellow); }
  .technician-heading {
    position: absolute; left: 0; width: 100%; top: 559px; text-align: center;
    font-weight: 600; font-size: 18.5px; line-height: 25px; text-transform: uppercase;
  }
</style>
</head>
<body>
<svg width="0" height="0" style="position:absolute">
  <defs>
    <symbol id="tick" viewBox="0 0 22 22">
      <circle cx="11" cy="11" r="11" fill="#ece51e"/>
      <path d="M5.8 11.3 L9.4 14.8 L16.4 7.6" fill="none" stroke="#44434f" stroke-width="2.6" stroke-linecap="round" stroke-linejoin="round"/>
    </symbol>
  </defs>
</svg>

<main class="flyer">
  <div class="headline-frame"></div>
  <h1>
    <span class="title-line title-kicker">Commercial &amp; Industrial</span>
    <span class="title-line title-main">Kitchen Equipment</span>
    <span class="title-line title-sub">Services</span>
  </h1>
  <p class="tagline">WE HANDLE EVERYTHING FROM THE FRONT DOOR TO THE BACK DOOR.</p>

  <h2 class="section-heading">WE OFFER HOT AND COLD EQUIPMENT</h2>

  <div class="item service-chip" style="left:52px;top:392px"><svg class="tick"><use href="#tick"/></svg>Repair</div>
  <div class="item service-chip" style="left:169px;top:392px"><svg class="tick"><use href="#tick"/></svg>Cleaning</div>
  <div class="item service-chip" style="left:52px;top:432px"><svg class="tick"><use href="#tick"/></svg>Maintenance</div>
  <div class="item service-chip" style="left:222px;top:432px"><svg class="tick"><use href="#tick"/></svg>Handyman Work</div>
  <div class="item service-chip" style="left:52px;top:471px"><svg class="tick"><use href="#tick"/></svg>Drywall</div>
  <div class="item service-chip" style="left:192px;top:471px"><svg class="tick"><use href="#tick"/></svg>Painting</div>
  <div class="item service-chip" style="left:52px;top:511px"><svg class="tick"><use href="#tick"/></svg>Door Closers</div>
  <div class="item service-chip" style="left:239px;top:511px"><svg class="tick"><use href="#tick"/></svg>Floors, and Ceilingtiles</div>

  <p class="call-out" style="top:418px">FOR ANY NEED IN YOUR RESTAURANT</p>
  <p class="call-out call-out--accent" style="top:446px">CALL US AND WE WILL SEND</p>

  <h2 class="technician-heading">A skilled technician to manage all your commercial<br>and industrial facility requirements</h2>

  <div class="item feature" style="left:48px;top:625px"><svg class="tick"><use href="#tick"/></svg>NKSTA Certified Technicians</div>
  <div class="item feature" style="left:327px;top:625px"><svg class="tick"><use href="#tick"/></svg>Round-the-clock emergency services</div>

  <div class="item feature" style="left:48px;top:669px;width:740px"><svg class="tick"><use href="#tick"/></svg><span>Customers who subscribe to preventive maintenance services receive a reduced rate on<br>hourly labor charges.</span></div>

  <div class="item feature" style="left:48px;top:722px"><svg class="tick"><use href="#tick"/></svg>Round-the-clock emergency services</div>
  <div class="item feature" style="left:382px;top:722px"><svg class="tick"><use href="#tick"/></svg>Original equipment manufacturer (OEM) parts</div>

  <div class="item feature" style="left:48px;top:765px"><svg class="tick"><use href="#tick"/></svg>30-day warranty on all OEM parts installed</div>
  <div class="item feature" style="left:415px;top:765px"><svg class="tick"><use href="#tick"/></svg>Equipment Cleaning &amp; Rebuilds</div>

  <div class="item feature" style="left:48px;top:807px"><svg class="tick"><use href="#tick"/></svg>Used equipment available for purchase or rental</div>
  <div class="item feature" style="left:461px;top:807px"><svg class="tick"><use href="#tick"/></svg>Equipment Cleaning &amp; Rebuilds</div>

  <div class="item feature" style="left:48px;top:846px"><svg class="tick"><use href="#tick"/></svg><span>Specialized Programs for Preventive Maintenance<br>of Equipment</span></div>
  <div class="item feature" style="left:466px;top:846px"><svg class="tick"><use href="#tick"/></svg><span>Installation and Repair of Restaurant<br>Equipment</span></div>

  <div class="item feature" style="left:48px;top:896px"><svg class="tick"><use href="#tick"/></svg>Repair or replace restaurant furniture</div>
  <div class="item feature" style="left:403px;top:896px"><svg class="tick"><use href="#tick"/></svg>Building Graffiti Removal Services</div>

  <div class="item feature" style="left:48px;top:941px;width:750px"><svg class="tick"><use href="#tick"/></svg><span>Comprehensive licensed electrical contractor services for both interior and exterior projects,<br>including lighting system upgrades</span></div>

  <div class="item feature" style="left:48px;top:996px"><svg class="tick"><use href="#tick"/></svg>Hot &amp; Cold Equipment</div>
  <div class="item feature" style="left:396px;top:996px"><svg class="tick"><use href="#tick"/></svg>Food Service Trucks</div>

  <div class="item feature" style="left:48px;top:1037px;width:750px"><svg class="tick"><use href="#tick"/></svg><span>We repair floors, walls, counters, décor, signage, parking lots, dumpsters, and more. If you<br>have it, we probably fix it</span></div>
</main>
</body>
</html>
```